Front and back cover design for skincare marketing materials

Thank you for showing an interest in my project.
Project Details.

I require a front and back cover for our marketing materials.
·       Front Cover size: 105 mm W x 150 mm H.
·       Back Cover size:  105 mm W x 150 mm H.
·       It must include these two colors. You can use a third color if you wish.
1.     #DBA09D
2.     #FFFFFF
 
Front Cover
·      The front cover will have a faded image of the Kakadu Plum branch and fruit. There are two image files, KP_image-1.jpg and kp_image-2.jpeg. You can use both images, just a portion of them, or source alternative royalty-free images of Kakadu Plum that may better fit the design. These two files have been uploaded.
 
The front cover wording.
Top of the front cover.
a.     The title of the image. “Kakadu Plum”
b.     The brand name, “Velvora Skincare”. The file brand_name.ai uploaded.
 
Bottom of the front cover- Designer's choice of font.
The bottom of the front cover contains three lines of text in the following order.  
1.     Australian Native Ingredients
2.     100% Natural · Organic · Wild-harvested
3.     Australian-Made Premium Skincare
 
Back Cover
·      Back Cover wording.The back cover contains the following words "grown by nature" in white (#FFFFFF) of font Italianno (font_file.ttf) with a background color of #DBA09D as seen in the sample box (sample_box.pdf) right-side panel
 
Please provide one file for the front cover and a separate file for the back cover.
All the elements of the files must be editable.
 
Do NOT use the Curve function on the files, as the text must remain editable/changeable.
 
All assets/resources/files, including fonts not supplied by us but used by the designer, must be named and provided with the finished design.

Target Market(s)

Beauty-minded Asian consumers between the ages of 32 and 75 who take a proactive approach to maintaining younger-looking skin. Those who already know the danger of skin damage caused by skincare containing harsh chemicals choose effective natural/organic solutions to meet their skincare needs. Those who wish a more radiant glow and youthful appearance to their skin. Usually, a two-income middle to high-income bracket couples with a mindset for health and beauty.

Industry/Entity Type

beauty

Font styles to use
Other font styles liked:
• I will provide a font file and a brand name file.

Requirements
Must have
• You must use the two colors provided on the product box. The designer may use a third color.
Nice to have
• some gold colour

```html
<!DOCTYPE html>
<html lang="en">
<head>
<meta charset="utf-8">
<title>Velvora Skincare – Kakadu Plum Covers</title>
<link rel="stylesheet" href="https://fonts.googleapis.com/css2?family=Italianno&family=Barlow+Condensed:wght@300&display=swap">
<style>
  :root {
    --backdrop: #d3d3d3;
    --paper: #ffffff;
    --rose: #dba09d;
    --rose-light: #e6bfbd;
    --rose-deep: #cf9593;
    --ink: #4a4a4a;
    --leaf-light: #b9d88a;
    --leaf: #7fb04e;
  }
  * { margin: 0; padding: 0; box-sizing: border-box; }
  html, body {
    width: 1200px;
    height: 848px;
    overflow: hidden;
    background: var(--backdrop);
  }
  .stage {
    position: relative;
    width: 1200px;
    height: 848px;
    display: flex;
    justify-content: center;
    align-items: center;
    gap: 80px;
  }
  .cover {
    position: relative;
    width: 434px;
    height: 620px;
    box-shadow: 6px 8px 14px rgba(0, 0, 0, 0.18);
  }
  /* Front cover */
  .cover--front {
    background: var(--paper);
    text-align: center;
  }
  .brand {
    position: absolute;
    top: 48px;
    left: 0;
    width: 100%;
    font-family: "Italianno", cursive;
    font-weight: 400;
    color: var(--rose);
    line-height: 1;
  }
  .brand__name {
    display: block;
    font-size: 104px;
  }
  .brand__line {
    display: block;
    font-size: 34px;
    margin-top: -8px;
  }
  .product-title {
    position: absolute;
    top: 186px;
    left: 0;
    width: 100%;
    font-family: "Italianno", cursive;
    font-weight: 400;
    font-size: 56px;
    color: var(--ink);
    line-height: 1;
  }
  .illustration {
    position: absolute;
    top: 246px;
    left: 105px;
    width: 224px;
    height: 254px;
    background: linear-gradient(160deg, var(--leaf-light) 0%, var(--leaf) 100%);
  }
  .claims {
    position: absolute;
    top: 508px;
    left: 0;
    width: 100%;
    list-style: none;
    font-family: "Barlow Condensed", sans-serif;
    font-weight: 300;
    font-size: 17.5px;
    line-height: 23.5px;
    color: var(--ink);
  }
  /* Back cover */
  .cover--back {
    background: linear-gradient(160deg, var(--rose-light) 0%, var(--rose) 55%, var(--rose-deep) 100%);
  }
  .tagline {
    position: absolute;
    top: 360px;
    left: 0;
    width: 100%;
    text-align: center;
    font-family: "Italianno", cursive;
    font-weight: 400;
    font-size: 50px;
    color: var(--paper);
    line-height: 1;
  }
</style>
</head>
<body>
  <main class="stage">
    <section class="cover cover--front" aria-label="Front cover">
      <h1 class="brand">
        <span class="brand__name">Velvora</span>
        <span class="brand__line">Skincare</span>
      </h1>
      <h2 class="product-title">Kakadu Plum</h2>
      <div class="illustration" role="img" aria-label="Painted illustration of a Kakadu plum branch with green leaves and ripening fruit"></div>
      <ul class="claims">
        <li>Australian Native Ingredients</li>
        <li>100% Natural · Organic · Wild-harvested</li>
        <li>Australian-Made Premium Skincare</li>
      </ul>
    </section>
    <section class="cover cover--back" aria-label="Back cover">
      <p class="tagline">Grown By Nature</p>
    </section>
  </main>
</body>
</html>
```